Letterhead Design for Law Firm that Specializes in Property Damage Litigation

We are looking for a redesign of our letterhead. Our current letterhead lists all of our current staff members and we'd like to come up with a design that does NOT list all of the staff members so that it does not need to be updated with every newly hired employee. Must be in editable format.

We are a law firm that specializes in property damage, so we need something that is professional, yet modern. The final design should use our existing logo and should use a blue color scheme (alternate colors would be gray, black, and white).

Industry/Entity Type

Legal

Colors
0054AA
0677BA
7BADD7
CADEEF
E8F1F8

```html
<!DOCTYPE html>
<html lang="en">
<head>
<meta charset="utf-8">
<title>Harrow Lindqvist and Pell — Stationery</title>
<link rel="stylesheet" href="https://fonts.googleapis.com/css2?family=Tinos:wght@400;700&family=Montserrat:wght@400;600&family=League+Spartan:wght@600&family=Didact+Gothic&family=Open+Sans:wght@600&display=swap">
<style>
  :root{
    --navy:#243a66;
    --gray:#6b6b6b;
    --text-gray:#8a8a8a;
    --paper:#f1f1f1;
    --backdrop:#c2c2c2;
    --rule:#5a6784;
    --white:#ffffff;
  }
  *{box-sizing:border-box;margin:0;padding:0}
  html,body{width:1200px;height:1144px;overflow:hidden;background:var(--backdrop)}
  .canvas{position:relative;width:1200px;height:1144px}
  .icon-defs{position:absolute;width:0;height:0}
  .ico{width:10px;height:10px;vertical-align:-1px;fill:var(--navy)}

  /* Firm name (plain wordmark) */
  .firm-name{font-family:"Montserrat",sans-serif;font-weight:600;color:var(--navy);white-space:nowrap;display:flex;align-items:center;gap:8px}
  .firm-name::before{content:"";display:block;width:10px;height:10px;background:currentColor;flex:none}

  /* Letterhead */
  .letterhead{position:absolute;left:30px;top:34px;width:760px;height:1076px;background:var(--paper);overflow:hidden}
  .letterhead .firm-name{position:absolute;left:29px;top:78px;font-size:17px}
  .sender{position:absolute;right:29px;top:40px;text-align:right;font-family:"Montserrat",sans-serif;color:var(--gray);font-size:11.5px;line-height:15px}
  .sender .sender-name{font-family:"Tinos",serif;color:var(--navy);font-size:13.5px;margin-bottom:2px}
  .sender .sender-name span{color:var(--gray)}
  .header-rule{position:absolute;left:27px;right:29px;top:133px;height:1px;background:var(--rule)}
  .recipient{position:absolute;left:43px;top:196px;font-family:"Montserrat",sans-serif;color:var(--text-gray);font-size:13px;line-height:18px}
  .recipient-name{font-family:"League Spartan",sans-serif;font-weight:600;color:var(--navy);font-size:25px;line-height:28px;margin-bottom:7px}
  .recipient p{margin-bottom:6px}
  .letter-date{position:absolute;right:41px;top:288px;font-family:"Open Sans",sans-serif;font-weight:600;color:var(--text-gray);font-size:14.5px}
  .letter-body{position:absolute;left:39px;width:680px;font-family:"Didact Gothic",sans-serif;color:var(--text-gray);font-size:13.4px;line-height:17.9px;text-align:justify}
  .p1{top:342px}.p2{top:467px}.p3{top:592px}
  .signature{position:absolute;left:500px;top:840px;width:100px;height:50px;background:linear-gradient(90deg,#e4e4e4,#dcdcdc);border-radius:3px}
  .offices{position:absolute;top:973px;font-family:"Montserrat",sans-serif;color:var(--text-gray);font-size:10.2px;line-height:16px}
  .office-title{font-family:"Tinos",serif;font-weight:700;color:var(--navy);font-size:13px;letter-spacing:.4px;margin-bottom:2px}
  .office-line{display:flex;gap:4px}
  .office-line .ico{flex:none;margin-top:3px}
  .office-philly{left:160px}.office-nj{left:332px}
  .admissions{position:absolute;left:508px;top:988px;font-family:"Montserrat",sans-serif;color:var(--text-gray);font-size:9.6px;line-height:15px}
  .footer-band{position:absolute;left:0;right:0;bottom:0;height:10px;background:var(--navy)}

  /* Business cards */
  .card{position:absolute;left:836px;width:340px;height:210px;overflow:hidden}
  .card-front{top:300px;background:var(--navy);display:flex;align-items:center;justify-content:center}
  .card-front .firm-name{color:var(--white);font-size:17px}
  .card-back{top:570px;background:var(--paper)}
  .card-back .firm-name{position:absolute;left:18px;top:22px;font-size:10px;gap:5px}
  .card-back .firm-name::before{width:7px;height:7px}
  .card-holder{position:absolute;right:18px;top:16px;text-align:right;font-family:"Tinos",serif;color:var(--navy)}
  .card-holder-name{font-size:20px;line-height:22px}
  .card-holder-title{font-size:11.5px;color:var(--gray)}
  .card-contacts{position:absolute;right:18px;top:66px;text-align:right;font-family:"Montserrat",sans-serif;color:var(--gray);font-size:8px;line-height:14.5px}
  .card-contacts .ico{width:8px;height:8px;margin-left:4px}
  .card-office{position:absolute;top:160px;font-family:"Montserrat",sans-serif;color:var(--gray);font-size:5.6px;line-height:7.6px}
  .card-office h3{font-family:"Tinos",serif;font-weight:700;color:var(--navy);font-size:7px;letter-spacing:.3px;margin-bottom:2px}
  .card-office-philly{left:126px}
  .card-office-nj{right:18px;text-align:right}
  .card-band{position:absolute;left:0;right:0;bottom:0;height:3px;background:var(--navy)}
</style>
</head>
<body>
<div class="canvas">

  <svg class="icon-defs" aria-hidden="true">
    <symbol id="i-phone" viewBox="0 0 20 20"><circle cx="10" cy="10" r="10"/><path fill="#fff" d="M6.5 5h2l1 2.6-1.3 1c.6 1.3 1.6 2.3 2.9 2.9l1-1.3 2.6 1v2c0 .6-.5 1-1.1 1C9 14.2 5.8 11 5.5 6.1 5.5 5.5 5.9 5 6.5 5z"/></symbol>
    <symbol id="i-fax" viewBox="0 0 20 20"><circle cx="10" cy="10" r="10"/><path fill="#fff" d="M7 5h6v3H7zM5 8.5h10v5h-2v-2H7v2H5zM7.5 12h5v3h-5z"/></symbol>
    <symbol id="i-pin" viewBox="0 0 20 20"><circle cx="10" cy="10" r="10"/><path fill="#fff" d="M10 4a4 4 0 0 1 4 4c0 3-4 8-4 8s-4-5-4-8a4 4 0 0 1 4-4zm0 2.4a1.6 1.6 0 1 0 0 3.2 1.6 1.6 0 0 0 0-3.2z"/></symbol>
    <symbol id="i-globe" viewBox="0 0 20 20"><circle cx="10" cy="10" r="10"/><g fill="none" stroke="#fff" stroke-width="1.2"><circle cx="10" cy="10" r="5.2"/><ellipse cx="10" cy="10" rx="2.2" ry="5.2"/><path d="M4.8 10h10.4"/></g></symbol>
    <symbol id="i-mail" viewBox="0 0 20 20"><circle cx="10" cy="10" r="10"/><rect x="5" y="6.5" width="10" height="7" fill="#fff"/><path d="M5 6.8l5 3.8 5-3.8" fill="none" stroke="#243a66" stroke-width="1"/></symbol>
  </svg>

  <!-- Letterhead -->
  <section class="letterhead" aria-label="Letterhead">
    <div class="firm-name">Harrow Lindqvist and Pell</div>

    <div class="sender">
      <div class="sender-name">Marcus Halvorsen, <span>Esquire</span></div>
      <div>mhalvorsen@hlplegal.com</div>
      <div>(215) 555-0142 <svg class="ico"><use href="#i-phone"/></svg></div>
      <div>www.hlplegal.com <svg class="ico"><use href="#i-globe"/></svg></div>
    </div>

    <div class="header-rule"></div>

    <div class="recipient">
      <div class="recipient-name">JONE SMITH</div>
      <p>0123-456-789</p>
      <p>mhalvorsen@hlplegal.com</p>
      <p>1234 City Your Ln. Suite<br>123 Dallas, TX 0000</p>
    </div>

    <div class="letter-date">12 December, 2023</div>

    <p class="letter-body p1">Lorem ipsum dolor sit amet, consectetuer adipiscing elit, sed diam nonummy nibh euismod tincidunt ut laoreet dolore magna aliquam erat volutpat. Ut wisi enim ad minim veniam, quis nostrud exerci tation ullamcorper suscipit lobortis nisl ut aliquip ex ea commodo consequat. Duis autem vel eum iriure dolor in hendrerit in vulputate velit esse molestie consequat, vel illum dolore eu feugiat nulla facilisis at vero eros et accumsan et iusto odio dignissim qui blandit praesent luptatum zzril delenit augue duis dolore te feugait nulla facilisi.</p>

    <p class="letter-body p2">Lorem ipsum dolor sit amet, cons ectetuer adipiscing elit, sed diam nonummy nibh euismod tincidunt ut laoreet dolore magna aliquam erat volutpat. Ut wisi enim ad minim veniam, quis nostrud exerci tation ullamcorper suscipit lobortis nisl ut aliquip ex ea commodo consequat.<br>Lorem ipsum dolor sit amet, consectetuer adipiscing elit, sed diam nonummy nibh euismod tincidunt ut laoreet dolore magna aliquam erat</p>

    <p class="letter-body p3">Lorem ipsum dolor sit amet, cons ectetuer adipiscing elit, sed diam nonummy nibh euismod tincidunt ut laoreet dolore magna aliquam erat volutpat. Ut wisi enim ad minim veniam, quis nostrud exerci tation ullamcorper suscipit lobortis nisl ut aliquip ex ea commodo consequat. Lorem ipsum dolor sit zamet, consectetuer adipiscing elit, sed diam nonummy nibh euismod tincidunt. Lorem ipsum dolor sit amet, cons ectetuer adipiscing elit, sed diam nonummy nibh euismod tincidunt ut laoreet dolore magna aliquam erat volutpat. Ut wisi enim ad minim veniam, quis nostrud exerci tation ullamcorper suscipit lobortis nisl ut aliquip ex ea commodo consequat. Lorem ipsum dolor sit zamet, consectetuer adipiscing elit, sed diam nonummy nibh euismod tincidunt. Lorem ipsum dolor sit amet, cons ectetuer adipiscing elit, sed diam nonummy nibh euismod tincidunt ut laoreet dolore magna aliquam erat volutpat. Ut wisi enim ad minim veniam, quis nostrud exerci tation ullamcorper suscipit lobortis nisl ut aliquip ex ea commodo consequat. Lorem ipsum dolor sit zamet, consectetuer adipiscing elit, sed diam nonummy nibh.</p>

    <div class="signature" role="img" aria-label="Handwritten signature of the sender"></div>

    <div class="offices office-philly">
      <div class="office-title">PHILADELPHIA OFFICE</div>
      <div class="office-line"><svg class="ico"><use href="#i-phone"/></svg><span>215.555.0142</span></div>
      <div class="office-line"><svg class="ico"><use href="#i-fax"/></svg><span>215.555.0187</span></div>
      <div class="office-line"><svg class="ico"><use href="#i-pin"/></svg><span>420 Market Street Suite 900<br>Philadelphia, PA 19106</span></div>
    </div>

    <div class="offices office-nj">
      <div class="office-title">NEW JERSEY OFFICE</div>
      <div class="office-line"><svg class="ico"><use href="#i-phone"/></svg><span>856.555.0163</span></div>
      <div class="office-line"><svg class="ico"><use href="#i-fax"/></svg><span>215.555.0187</span></div>
      <div class="office-line"><svg class="ico"><use href="#i-pin"/></svg><span>75 Haddon Avenue North<br>Suite 310 Cherry Hill, NJ 08002</span></div>
    </div>

    <div class="admissions">
      Admitted to PA &amp; NJ Bars<br>
      *Admitted to PA Bar Only<br>
      *Admitted to PA Bar,<br>
      Pending Admission to NJ Bar
    </div>

    <div class="footer-band"></div>
  </section>

  <!-- Business card, front -->
  <section class="card card-front" aria-label="Business card front">
    <div class="firm-name">Harrow Lindqvist and Pell</div>
  </section>

  <!-- Business card, back -->
  <section class="card card-back" aria-label="Business card back">
    <div class="firm-name">Harrow Lindqvist and Pell</div>
    <div class="card-holder">
      <div class="card-holder-name">Marcus Halvorsen</div>
      <div class="card-holder-title">Esquire</div>
    </div>
    <div class="card-contacts">
      <div>(215) 555-0142<svg class="ico"><use href="#i-phone"/></svg></div>
      <div>mhalvorsen@hlplegal.com<svg class="ico"><use href="#i-mail"/></svg></div>
      <div>www.hlplegal.com<svg class="ico"><use href="#i-globe"/></svg></div>
    </div>
    <div class="card-office card-office-philly">
      <h3>PHILADELPHIA OFFICE</h3>
      420 Market Street<br>Suite 900<br>Philadelphia, PA 19106
    </div>
    <div class="card-office card-office-nj">
      <h3>NEW JERSEY OFFICE</h3>
      75 Haddon Avenue<br>North Suite<br>310 Cherry Hill, NJ 08002
    </div>
    <div class="card-band"></div>
  </section>

</div>
</body>
</html>
```